Mobile App design improvement- Figma

I have four screens need to redesign, and I have the design guide to help you.
The goal is to make the design clean and easy to understand CTA improve UI/UX. You can change the icons, and don't change the fonts or color. Also, if you are doing a great job, I will hire you finish the rest of the design of the app.
Here is our site: https://bellowpine.com
BellowPine App is wishlist:
Hight features and app propositions of the app collaborative shopping and chatting with invited friends and family. Easily to get feedback and make decisions of the products from friends, chat, vote, poll, compare.
Here is the Figma link: https://www.mockboard.example/design/XqTT4LmW82pHd7ZsKe9UvN/BellowPine--App?node-id=31-55102&t=HgRw7NbZp3QeLm5Ky-2
Here is the app links:
IOS app:
https://lnk.example/8QeTp2r

Android app:
https://lnk.example/8QeTp2k
Updates

1. I need to have more design ideas that makes users feel simple and easy to understudy platforms can add products from search products, paste url, and use share button to add proton there wishlist from other e-commerce sites. Simplify the search, paste url, and user share button page, maybe combine search with paste url in the search bar, or switch back and forth with search key, paste URL, or share product from other e-commerce sites. Shop page, maybe show users to pick favorites brands recommended products and popular brands. My profile page, I need to be simple but also give users ability to navigate between the save money and wishlists. Please don’t change my color of the app header and color theme. Tone: Ecommerce marketplace, social media, fun! Highlights invite friends chat, save money, and add product.

Target Market(s)

female CEOs, moms, female interns

Industry/Entity Type

Social networking, shopping.

Number of Pages Required

4 page

Font styles to use
Other font styles liked:
• please look at our brand guide

Requirements
Nice to have
• Simple design, highlight invite memebers, and highlight 3 options for them to get products into one place. Highlight collabrative and social tone.
Should not have
• Don't give me too much colors.

```html
<!DOCTYPE html>
<html lang="en">
<head>
<meta charset="utf-8">
<title>BellowPine App – Shop</title>
<link href="https://fonts.googleapis.com/css2?family=Plus+Jakarta+Sans:wght@400;500;600;700&family=Inter:wght@400;500;600&display=swap" rel="stylesheet">
<style>
  :root {
    --header-yellow: #fbd45a;
    --sun-yellow: #fde7a4;
    --brand-violet: #4733c8;
    --title-violet: #4a35c8;
    --ink: #2b2b33;
    --muted: #8a8a90;
    --field-bg: #f1f1f2;
    --divider: #e4e4e7;
    --white: #ffffff;
    --kb-bg: #d2d5db;
    --kb-key: #ffffff;
    --kb-key-alt: #abb0ba;
    --kb-ink: #111111;
    --kb-shadow: #8a8e96;
    --kb-icon: #4a4d53;
  }
  * { box-sizing: border-box; margin: 0; padding: 0; }
  html, body { width: 1200px; height: 2602px; overflow: hidden; background: var(--white); }
  .screen {
    position: absolute; left: 0; top: 0;
    width: 393px; height: 852px;
    transform: scale(3.0534); transform-origin: 0 0;
    background: var(--header-yellow);
    overflow: hidden;
    font-family: "Plus Jakarta Sans", sans-serif;
  }
  .status-bar { position: absolute; left: 0; top: 0; width: 393px; height: 55px; color: var(--white); }
  .status-time { position: absolute; left: 52px; top: 21px; font-family: "Inter", sans-serif; font-weight: 600; font-size: 17px; line-height: 22px; }
  .status-icons { position: absolute; right: 36px; top: 26px; }
  .sheet {
    position: absolute; left: 0; top: 55px; width: 393px; height: 797px;
    background: var(--white); border-radius: 46px 46px 0 0;
  }
  .app-header { position: absolute; left: 0; top: 0; width: 393px; height: 80px; }
  .app-header .back { position: absolute; left: 22px; top: 34px; }
  .app-header .menu { position: absolute; right: 22px; top: 36px; }
  .app-header h1 { position: absolute; left: 0; right: 0; top: 27px; text-align: center; font-size: 20px; line-height: 24px; font-weight: 500; color: var(--ink); }
  .hero { position: absolute; left: 0; top: 100px; width: 393px; height: 186px; overflow: hidden; }
  .hero-sun { position: absolute; left: 79px; top: 74px; width: 224px; height: 224px; border-radius: 50%; background: var(--sun-yellow); }
  .hero-mascot {
    position: absolute; left: 124px; top: 28px; width: 126px; height: 158px;
    border-radius: 50px 50px 24px 24px;
    background: linear-gradient(180deg, #8b87c4 0%, #7772b5 70%, #6a66ad 100%);
  }
  .hero-divider { position: absolute; left: 0; top: 286px; width: 393px; height: 1px; background: var(--divider); }
  .intro { position: absolute; left: 0; top: 308px; width: 393px; text-align: center; }
  .intro .eyebrow { font-size: 15px; line-height: 19px; color: var(--muted); font-weight: 400; }
  .intro h2 { margin-top: 3px; font-size: 19px; line-height: 25px; font-weight: 700; color: var(--title-violet); }
  .search-field {
    position: absolute; left: 25px; top: 405px; width: 337px; height: 52px;
    border-radius: 26px; background: var(--field-bg);
    display: flex; align-items: center; padding-left: 15px; gap: 4px;
    font-size: 14px; font-weight: 600; color: var(--ink);
  }
  .paste-button {
    position: absolute; left: 25px; top: 473px; width: 337px; height: 58px;
    border-radius: 29px; background: var(--brand-violet); color: var(--white);
    display: flex; align-items: flex-start; justify-content: center; gap: 12px; padding-top: 19px;
    font-size: 14px; line-height: 18px; font-weight: 500;
  }
  .keyboard {
    position: absolute; left: 0; top: 571px; width: 393px; height: 281px;
    background: var(--kb-bg); font-family: "Inter", sans-serif; color: var(--kb-ink);
  }
  .kb-row { position: absolute; left: 0; width: 393px; display: flex; gap: 5.6px; }
  .kb-row.r1 { top: 13px; padding-left: 10px; }
  .kb-row.r2 { top: 67px; padding-left: 29px; }
  .kb-row.r3 { top: 121px; padding-left: 10px; }
  .kb-row.r4 { top: 165px; padding-left: 10px; gap: 6px; }
  .key {
    width: 32px; height: 42px; border-radius: 5px; background: var(--kb-key);
    box-shadow: 0 1px 0 var(--kb-shadow);
    display: flex; align-items: center; justify-content: center;
    font-size: 22px; font-weight: 400;
  }
  .key.alt { background: var(--kb-key-alt); }
  .key.shift, .key.delete { width: 43px; }
  .kb-row.r3 .letters { display: flex; gap: 5.6px; margin: 0 14px; }
  .key.numbers { width: 89px; font-size: 15px; }
  .key.space { width: 183px; font-size: 15px; }
  .key.search { width: 89px; font-size: 15px; color: #6e737b; }
  .kb-emoji { position: absolute; left: 36px; top: 229px; }
  .kb-mic { position: absolute; left: 333px; top: 228px; }
  .home-indicator { position: absolute; left: 130px; top: 268px; width: 134px; height: 5px; border-radius: 3px; background: #000; }
</style>
</head>
<body>
<div class="screen">
  <div class="status-bar">
    <span class="status-time">9:41</span>
    <svg class="status-icons" width="76" height="13" viewBox="0 0 76 13" fill="#fff">
      <rect x="0" y="8" width="3" height="4" rx="1"/><rect x="5" y="6" width="3" height="6" rx="1"/>
      <rect x="10" y="3" width="3" height="9" rx="1"/><rect x="15" y="0" width="3" height="12" rx="1"/>
      <path d="M31 11.5l-2.2-2.3a3.2 3.2 0 0 1 4.4 0zM26.6 7a6.4 6.4 0 0 1 8.8 0l-1.3 1.3a4.6 4.6 0 0 0-6.2 0zM24.3 4.7a9.7 9.7 0 0 1 13.4 0l-1.3 1.3a7.9 7.9 0 0 0-10.8 0z"/>
      <rect x="49" y="0.5" width="23" height="12" rx="3.5" fill="none" stroke="#fff" stroke-opacity=".5"/>
      <rect x="51" y="2.5" width="19" height="8" rx="2"/><rect x="73.5" y="4.5" width="1.5" height="4" rx=".7" fill-opacity=".5"/>
    </svg>
  </div>

  <main class="sheet">
    <header class="app-header">
      <svg class="back" width="18" height="16" viewBox="0 0 18 16" fill="none" stroke="#2b2b33" stroke-width="1.8" stroke-linecap="round" stroke-linejoin="round"><path d="M17 8H1.5M8 1.5L1.5 8 8 14.5"/></svg>
      <h1>Shop</h1>
      <svg class="menu" width="18" height="14" viewBox="0 0 18 14" stroke="#2b2b33" stroke-width="1.8" stroke-linecap="round"><path d="M1 1h16M1 7h16M1 13h16"/></svg>
    </header>

    <section class="hero">
      <div class="hero-sun"></div>
      <div class="hero-mascot" role="img" aria-label="Mascot illustration holding a phone"></div>
    </section>
    <div class="hero-divider"></div>

    <section class="intro">
      <p class="eyebrow">Shop</p>
      <h2>Search your Product<br>or Paste&nbsp; Product Link</h2>
    </section>

    <label class="search-field" aria-label="Search products or paste a product link">
      <svg width="20" height="20" viewBox="0 0 20 20" fill="none" stroke="#2b2b33" stroke-width="1.6" stroke-linecap="round"><circle cx="8.5" cy="8.5" r="6.5"/><path d="M13.5 13.5L18 18"/></svg>
      <span>Ni</span>
    </label>

    <div class="paste-button">
      <svg width="16" height="19" viewBox="0 0 16 19" fill="none" stroke="#fff" stroke-width="1.6" stroke-linejoin="round"><rect x="1" y="3" width="14" height="15" rx="2"/><rect x="5" y="1" width="6" height="4" rx="1"/></svg>
      <span>Paste Product Link</span>
    </div>
  </main>

  <div class="keyboard">
    <div class="kb-row r1">
      <div class="key">q</div><div class="key">w</div><div class="key">e</div><div class="key">r</div><div class="key">t</div><div class="key">y</div><div class="key">u</div><div class="key">i</div><div class="key">o</div><div class="key">p</div>
    </div>
    <div class="kb-row r2">
      <div class="key">a</div><div class="key">s</div><div class="key">d</div><div class="key">f</div><div class="key">g</div><div class="key">h</div><div class="key">j</div><div class="key">k</div><div class="key">l</div>
    </div>
    <div class="kb-row r3">
      <div class="key alt shift"><svg width="20" height="18" viewBox="0 0 20 18" fill="none" stroke="#111" stroke-width="1.5" stroke-linejoin="round"><path d="M10 1.5L1.5 10H6v6.5h8V10h4.5z"/></svg></div>
      <div class="letters">
        <div class="key">z</div><div class="key">x</div><div class="key">c</div><div class="key">v</div><div class="key">b</div><div class="key">n</div><div class="key">m</div>
      </div>
      <div class="key alt delete"><svg width="24" height="18" viewBox="0 0 24 18" fill="none" stroke="#111" stroke-width="1.5" stroke-linejoin="round" stroke-linecap="round"><path d="M8 1.5h14v15H8L1.5 9z"/><path d="M11.5 5.5l7 7M18.5 5.5l-7 7"/></svg></div>
    </div>
    <div class="kb-row r4">
      <div class="key alt numbers">123</div>
      <div class="key space">space</div>
      <div class="key alt search">search</div>
    </div>
    <svg class="kb-emoji" width="26" height="26" viewBox="0 0 26 26" fill="none" stroke="#4a4d53" stroke-width="1.6" stroke-linecap="round"><circle cx="13" cy="13" r="11.5"/><circle cx="9" cy="10" r="1" fill="#4a4d53"/><circle cx="17" cy="10" r="1" fill="#4a4d53"/><path d="M7.5 15c1.5 3 9.5 3 11 0"/></svg>
    <svg class="kb-mic" width="18" height="28" viewBox="0 0 18 28" fill="none" stroke="#4a4d53" stroke-width="1.6" stroke-linecap="round"><rect x="5" y="1" width="8" height="16" rx="4"/><path d="M1.5 13a7.5 7.5 0 0 0 15 0M9 20.5V26M5 26h8"/></svg>
    <div class="home-indicator"></div>
  </div>
</div>
</body>
</html>
```